Increased budget: GUI redesign: 10 year old user interface needs modern look-and-feel

UPDATE: Please DO look at more than only th eone image I attached! Almost all designs are simply reworks of that one picture. That is not what we are looking for. Check out the video to understand what the product does, and try to make something better.
We have an existing app (see https://www.vornatek.com/downloadTunePilot.php?vers=3_9_1_140964&dir=Vornatek_OEM/3_9_1_140964&name=DSP_Control_Software) which needs refreshing. See also a video here: https://vornatek-oem.com/software/ and the user manual attached here. The GUI is now 800x400 pixels, which is too small; and not scalable, which will be fixed in the future. We need a new, modern look-and-feel, and images that can be exported from the design in various sizes. The current design is attached as well as a collection of PNG files. The overall layout can stay similar, although we are open to good ideas for improvements. The design should be targeted at professional users, not end users; the product is used by audio professionals (e.g. sound engineers, loudspeaker designers). Also see our web version: https://www.vornatek.com/tunepilot/skins/1_1_2/container.html?MAC=Demo%201x2
The winner will also be asked to do a full design of the application GUI (based on the design done here), with several more windows etc, and additional payment depending on the work to be done.

Target Market(s)

Professional audio

Industry/Entity Type

Audio / Industrial

Font styles to use
Other font styles liked:
• Futura (not mandatory)

Colors

Designer to choose colors to be used in the design.

Requirements
Must have
• Modern, timeless design, not too bling bling
Nice to have
• Flat design
Should not have
• 3D, bling bling, many colours, etc

```html
<!DOCTYPE html>
<html lang="en">
<head>
<meta charset="utf-8">
<title>Vornatek TunePilot – Output Channel</title>
<link href="https://fonts.googleapis.com/css2?family=Jost:wght@400;500;600;700&display=swap" rel="stylesheet">
<style>
:root{
  --bg:#1e1e1e;
  --shell:#262626;
  --sidebar:#0d0d0d;
  --panel:#262626;
  --btn:#1a1a1a;
  --field:#3a3a3a;
  --field-dark:#050505;
  --text:#ffffff;
  --muted:#cfcfcf;
  --accent:#f08a00;
  --tick:#8a8a8a;
  --graph:#000000;
  --grid:#5a5a5a;
  --meter-green:#2ee82e;
  --meter-dim:#2a8a2a;
  --meter-amber:#9a8a1a;
  --meter-red:#8a1a1a;
  --led-off:#2c2c2c;
}
*{box-sizing:border-box;margin:0;padding:0}
html,body{width:1200px;height:1200px;overflow:hidden;background:var(--bg);font-family:"Jost",sans-serif;color:var(--text)}
.canvas{position:relative;width:1200px;height:1200px}
.abs{position:absolute}
.shell{left:60px;top:310px;width:1080px;height:579px;background:var(--shell);border-radius:12px}
.sidebar{left:70px;top:320px;width:139px;height:560px;background:var(--sidebar);border-radius:8px}
.main{left:214px;top:320px;width:915px;height:560px;background:var(--panel);border-radius:8px}
.brand{left:100px;top:356px;width:80px;text-align:center;font-size:15px;font-weight:500;letter-spacing:.5px;color:var(--text)}
.nav-btn{left:80px;width:119px;height:28px;background:var(--btn);border-radius:4px;font-size:8px;display:flex;align-items:center;justify-content:center}
.nav-btn.active{background:var(--accent);font-weight:700}
.label{font-size:9px;color:var(--muted);line-height:1}
.title{font-size:13px;font-weight:700;color:#d8d8d8}
.col-head{font-size:13px;font-weight:700;color:#d8d8d8;transform:translateX(-50%)}
.fader-track{width:5px;background:#0a0a0a;border-radius:3px}
.fader-cap{width:20px;background:repeating-linear-gradient(#5a5a5a 0 2px,#3a3a3a 2px 4px);border-radius:3px}
.fader-cap::after{content:"";position:absolute;left:2px;right:2px;top:50%;height:1px;background:#ddd}
.scale-ticks{width:10px;background:repeating-linear-gradient(to bottom,var(--tick) 0 1px,transparent 1px 5.2px)}
.meter{width:7px;background:
  repeating-linear-gradient(to bottom,transparent 0 3px,#111 3px 4px),
  linear-gradient(to bottom,var(--meter-red) 0 6%,var(--meter-amber) 6% 28%,var(--meter-dim) 28% 38%,var(--meter-green) 38% 100%)}
.meter.master{background:
  repeating-linear-gradient(to bottom,transparent 0 3px,#111 3px 4px),
  linear-gradient(to bottom,var(--meter-red) 0 6%,var(--meter-amber) 6% 20%,var(--meter-dim) 20% 33%,var(--meter-green) 33% 100%)}
.value-box{height:19px;background:var(--field);border-radius:3px;font-size:8px;display:flex;align-items:center;justify-content:center;gap:18px}
.graph{left:586px;top:335px;width:403px;height:260px;background:var(--graph);border-radius:8px}
.field{height:28px;background:var(--field);border-radius:3px;font-size:8px;display:flex;align-items:center;justify-content:center}
.select{height:28px;background:var(--field-dark);border-radius:3px;font-size:8px;display:flex;align-items:center;justify-content:space-between;padding:0 7px}
.select::after{content:"";border-left:3.5px solid transparent;border-right:3.5px solid transparent;border-top:6px solid #fff}
.led{width:22px;height:22px;border-radius:50%;background:radial-gradient(circle,#444 0 2px,var(--led-off) 3px);border:1px solid #3a3a3a;transform:translate(-50%,-50%)}
.led.on{background:radial-gradient(circle,#9cff6a 0 2px,#3c7a2a 4px,#1e3a1a 10px)}
.led.red{background:radial-gradient(circle,#ff8080 0 2px,#a01a1a 5px,#3a1010 10px)}
.strip{left:904px;top:649px;width:204px;height:36px;background:#2a2a2a;border-radius:6px}
.section-head{font-size:12px;color:#d8d8d8;border-bottom:1px solid #9a9a9a;padding-bottom:1px}
.tag{font-size:7px;background:#4a4a4a;border-radius:2px;padding:1px 3px;color:#ddd}
.knob-label{font-size:11px;font-weight:700;color:#d8d8d8;transform:translateX(-50%)}
</style>
</head>
<body>
<div class="canvas">
  <div class="abs shell"></div>
  <div class="abs sidebar"></div>
  <div class="abs main"></div>

  <!-- Sidebar -->
  <div class="abs brand">VORNATEK</div>
  <div class="abs nav-btn" style="top:422px">Main</div>
  <div class="abs nav-btn" style="top:465px">X-over</div>
  <div class="abs nav-btn" style="top:509px">In 1</div>
  <div class="abs nav-btn" style="top:553px">In 2</div>
  <div class="abs nav-btn" style="top:597px">In 3</div>
  <div class="abs nav-btn" style="top:640px">In 4</div>
  <div class="abs nav-btn active" style="top:684px">Out 1</div>
  <div class="abs nav-btn" style="top:728px">Out 2</div>
  <div class="abs nav-btn" style="top:771px">Out 3</div>
  <div class="abs nav-btn" style="top:815px">Out 4</div>

  <!-- Mixer -->
  <div class="abs title" style="left:230px;top:335px">Mixer</div>
  <div class="abs label" style="left:239px;top:354px">0</div>
  <div class="abs label" style="left:232px;top:405px">-12</div>
  <div class="abs label" style="left:230px;top:457px">-24</div>
  <div class="abs label" style="left:230px;top:508px">-36</div>
  <div class="abs label" style="left:230px;top:559px">-48</div>
  <div class="abs label" style="left:560px;top:354px">0</div>
  <div class="abs label" style="left:553px;top:405px">-12</div>
  <div class="abs label" style="left:551px;top:457px">-24</div>
  <div class="abs label" style="left:551px;top:508px">-36</div>
  <div class="abs label" style="left:551px;top:559px">-48</div>

  <div class="abs scale-ticks" style="left:257px;top:357px;height:210px"></div>
  <div class="abs fader-track" style="left:269px;top:357px;height:210px"></div>
  <div class="abs fader-cap" style="left:261px;top:355px;height:43px"></div>
  <div class="abs meter" style="left:289px;top:355px;height:211px"></div>

  <div class="abs scale-ticks" style="left:333px;top:357px;height:210px"></div>
  <div class="abs fader-track" style="left:346px;top:357px;height:210px"></div>
  <div class="abs fader-cap" style="left:338px;top:334px;height:45px"></div>
  <div class="abs meter" style="left:365px;top:355px;height:211px"></div>

  <div class="abs scale-ticks" style="left:417px;top:357px;height:210px"></div>
  <div class="abs fader-track" style="left:430px;top:357px;height:210px"></div>
  <div class="abs fader-cap" style="left:422px;top:334px;height:45px"></div>
  <div class="abs meter" style="left:450px;top:355px;height:211px"></div>

  <div class="abs scale-ticks" style="left:493px;top:357px;height:210px"></div>
  <div class="abs fader-track" style="left:506px;top:357px;height:210px"></div>
  <div class="abs fader-cap" style="left:498px;top:334px;height:45px"></div>
  <div class="abs meter" style="left:525px;top:355px;height:211px"></div>
  <div class="abs scale-ticks" style="left:536px;top:357px;height:210px"></div>

  <div class="abs value-box" style="left:229px;top:576px;width:65px"><span>1</span><span>-6.00 dB</span></div>
  <div class="abs value-box" style="left:317px;top:576px;width:65px"><span>2</span><span>0.00 dB</span></div>
  <div class="abs value-box" style="left:402px;top:576px;width:65px"><span>3</span><span>0.00 dB</span></div>
  <div class="abs value-box" style="left:486px;top:576px;width:65px"><span>4</span><span>0.00 dB</span></div>

  <!-- EQ graph -->
  <div class="abs graph"></div>
  <svg class="abs" style="left:0;top:0" width="1200" height="1200" viewBox="0 0 1200 1200">
    <g stroke="var(--grid)" stroke-width="0.8" fill="none">
      <rect x="626" y="351" width="317" height="208"/>
      <path d="M658 351V559M689 351V559M721 351V559M753 351V559M784 351V559M816 351V559M848 351V559M879 351V559M911 351V559"/>
      <path d="M626 403H943M626 507H943"/>
    </g>
    <path d="M626 455H943" stroke="#bbb" stroke-width="0.8"/>
    <g fill="none" stroke="#ccc" stroke-width="1">
      <rect x="601" y="350" width="12" height="12" rx="2"/>
      <path d="M604 353l6 6M604 353h3M604 353v3M610 359h-3M610 359v-3"/>
      <rect x="601" y="374" width="12" height="12" rx="2"/>
      <circle cx="606.5" cy="379.5" r="2.5"/><path d="M608.5 381.5l2 2"/>
      <rect x="601" y="398" width="12" height="12" rx="2"/>
      <path d="M604 401.5h6M607 401.5v6"/>
    </g>
    <g font-family="Jost, sans-serif" font-size="8" fill="#fff" text-anchor="middle" dominant-baseline="central">
      <circle cx="656" cy="455" r="7.5" fill="#a3111b"/><text x="656" y="455">1</text>
      <circle cx="686" cy="455" r="7.5" fill="#a86a00"/><text x="686" y="455">2</text>
      <circle cx="715" cy="455" r="7.5" fill="#a09a00"/><text x="715" y="455">3</text>
      <circle cx="746" cy="455" r="7.5" fill="#1a991a"/><text x="746" y="455">4</text>
      <circle cx="776" cy="455" r="7.5" fill="#1a9aa5"/><text x="776" y="455">5</text>
      <circle cx="805" cy="455" r="7.5" fill="#1616b0"/><text x="805" y="455">6</text>
      <circle cx="835" cy="455" r="7.5" fill="#b01ab0"/><text x="835" y="455">7</text>
      <circle cx="866" cy="455" r="7.5" fill="#b03a08"/><text x="866" y="455">8</text>
      <circle cx="895" cy="455" r="7.5" fill="#9a8a0a"/><text x="895" y="455">9</text>
      <circle cx="926" cy="455" r="7.5" fill="#1ab81a"/><text x="926" y="455">10</text>
    </g>
    <g font-family="Jost, sans-serif" font-size="9" fill="#ddd" dominant-baseline="central">
      <text x="955" y="353">15</text><text x="955" y="387">10</text><text x="955" y="421">5</text>
      <text x="955" y="455">0dB</text><text x="955" y="489">- 5</text><text x="955" y="523">- 10</text><text x="955" y="557">- 15</text>
    </g>
    <g font-family="Jost, sans-serif" font-size="9" fill="#ddd" text-anchor="middle" dominant-baseline="central">
      <text x="605" y="577">10</text><text x="637" y="577">20</text><text x="669" y="577">50</text>
      <text x="703" y="577">100</text><text x="741" y="577">200</text><text x="779" y="577">500</text>
      <text x="813" y="577">1k</text><text x="843" y="577">2k</text><text x="874" y="577">5k</text>
      <text x="907" y="577">10k</text><text x="943" y="577">20k</text>
    </g>
    <!-- Knobs -->
    <g stroke="#777" stroke-width="0.7">
      <g id="ticks">
        <path d="M934 731v3M934 781v-3M909 756h3M959 756h-3M916 738l2 2M952 738l-2 2M916 774l2-2M952 774l-2-2M924 733l1 2.5M944 733l-1 2.5M911 746l2.5 1M957 746l-2.5 1M911 766l2.5-1M957 766l-2.5-1"/>
      </g>
      <use href="#ticks" x="72"/><use href="#ticks" x="143"/>
    </g>
    <defs>
      <radialGradient id="knobFace" cx="50%" cy="35%" r="65%">
        <stop offset="0" stop-color="#6a6a6a"/><stop offset="1" stop-color="#1a1a1a"/>
      </radialGradient>
    </defs>
    <circle cx="934" cy="756" r="18" fill="url(#knobFace)" stroke="#111"/>
    <path d="M926 765l4-4" stroke="#fff" stroke-width="1.6" stroke-linecap="round"/>
    <circle cx="1006" cy="756" r="18" fill="url(#knobFace)" stroke="#111"/>
    <path d="M1014 765l-4-4" stroke="#fff" stroke-width="1.6" stroke-linecap="round"/>
    <circle cx="1077" cy="756" r="18" fill="url(#knobFace)" stroke="#111"/>
    <path d="M1071 744l3 5" stroke="#fff" stroke-width="1.6" stroke-linecap="round"/>
  </svg>

  <!-- Master fader -->
  <div class="abs label" style="left:1011px;top:334px">+12</div>
  <div class="abs label" style="left:1013px;top:360px">+6</div>
  <div class="abs label" style="left:1018px;top:385px">0</div>
  <div class="abs label" style="left:1014px;top:410px">-6</div>
  <div class="abs label" style="left:1011px;top:436px">-12</div>
  <div class="abs label" style="left:1011px;top:461px">-18</div>
  <div class="abs label" style="left:1009px;top:487px">-24</div>
  <div class="abs label" style="left:1009px;top:512px">-30</div>
  <div class="abs label" style="left:1009px;top:537px">-36</div>
  <div class="abs label" style="left:1009px;top:563px">-42</div>
  <div class="abs label" style="left:1009px;top:588px">-48</div>
  <div class="abs scale-ticks" style="left:1033px;top:337px;height:256px"></div>
  <div class="abs fader-track" style="left:1048px;top:335px;height:259px"></div>
  <div class="abs fader-cap" style="left:1040px;top:384px;height:45px"></div>
  <div class="abs meter master" style="left:1069px;top:335px;height:259px"></div>
  <div class="abs scale-ticks" style="left:1079px;top:337px;height:256px"></div>
  <div class="abs label" style="left:1093px;top:334px">+12</div>
  <div class="abs label" style="left:1094px;top:360px">+6</div>
  <div class="abs label" style="left:1094px;top:385px">0</div>
  <div class="abs label" style="left:1094px;top:410px">-6</div>
  <div class="abs label" style="left:1094px;top:436px">-12</div>
  <div class="abs label" style="left:1094px;top:461px">-18</div>
  <div class="abs label" style="left:1094px;top:487px">-24</div>
  <div class="abs label" style="left:1094px;top:512px">-30</div>
  <div class="abs label" style="left:1094px;top:537px">-36</div>
  <div class="abs label" style="left:1094px;top:563px">-42</div>
  <div class="abs label" style="left:1094px;top:588px">-48</div>
  <div class="abs value-box" style="left:1008px;top:605px;width:63px">0.00 dB</div>

  <!-- Mute / Link -->
  <div class="abs strip"></div>
  <div class="abs" style="left:917px;top:661px;font-size:9px">Mute</div>
  <div class="abs led red" style="left:959px;top:667px"></div>
  <div class="abs" style="left:1005px;top:655px;width:1px;height:24px;background:#444"></div>
  <div class="abs" style="left:1040px;top:661px;font-size:9px">Link</div>
  <div class="abs led" style="left:1082px;top:667px"></div>

  <!-- Delay / Limiter -->
  <div class="abs section-head" style="left:902px;top:707px;width:64px">Delay</div>
  <div class="abs section-head" style="left:975px;top:707px;width:133px">Limiter</div>
  <div class="abs tag" style="left:1064px;top:709px">Compressor</div>
  <div class="abs value-box" style="left:902px;top:787px;width:64px">0.00 ms</div>
  <div class="abs value-box" style="left:975px;top:787px;width:64px">224 Vpk</div>
  <div class="abs value-box" style="left:1045px;top:787px;width:64px">50 dB/s</div>
  <div class="abs select" style="left:902px;top:811px;width:64px;height:20px;font-size:7px">ms</div>
  <div class="abs knob-label" style="left:1007px;top:811px">THR</div>
  <div class="abs knob-label" style="left:1077px;top:811px">REL</div>

  <!-- EQ bands: left block -->
  <div class="abs col-head" style="left:243px;top:609px">On</div>
  <div class="abs col-head" style="left:282px;top:609px;transform:none">Type</div>
  <div class="abs col-head" style="left:373px;top:609px">Freq</div>
  <div class="abs col-head" style="left:448px;top:609px">Q</div>
  <div class="abs col-head" style="left:498px;top:609px">Gain</div>

  <div class="abs led on" style="left:243px;top:645px"></div>
  <div class="abs select" style="left:262px;top:631px;width:87px">Bell</div>
  <div class="abs field" style="left:355px;top:631px;width:65px">20Hz</div>
  <div class="abs field" style="left:426px;top:631px;width:44px">1</div>
  <div class="abs field" style="left:476px;top:631px;width:45px">0dB</div>

  <div class="abs led" style="left:243px;top:678px"></div>
  <div class="abs select" style="left:262px;top:664px;width:87px">Notch</div>
  <div class="abs field" style="left:355px;top:664px;width:65px">20Hz</div>
  <div class="abs field" style="left:426px;top:664px;width:44px">1</div>
  <div class="abs field" style="left:476px;top:664px;width:45px">0dB</div>

  <div class="abs led" style="left:243px;top:712px"></div>
  <div class="abs select" style="left:262px;top:698px;width:87px">AllPass</div>
  <div class="abs field" style="left:355px;top:698px;width:65px">20Hz</div>
  <div class="abs field" style="left:426px;top:698px;width:44px">1</div>
  <div class="abs field" style="left:476px;top:698px;width:45px">0dB</div>

  <div class="abs led" style="left:243px;top:746px"></div>
  <div class="abs select" style="left:262px;top:732px;width:87px">Low Shelf</div>
  <div class="abs field" style="left:355px;top:732px;width:65px">20Hz</div>
  <div class="abs field" style="left:426px;top:732px;width:44px">1</div>
  <div class="abs field" style="left:476px;top:732px;width:45px">0dB</div>

  <div class="abs led" style="left:243px;top:779px"></div>
  <div class="abs select" style="left:262px;top:765px;width:87px">Band Pass</div>
  <div class="abs field" style="left:355px;top:765px;width:65px">20Hz</div>
  <div class="abs field" style="left:426px;top:765px;width:44px">1</div>
  <div class="abs field" style="left:476px;top:765px;width:45px">0dB</div>

  <div class="abs title" style="left:245px;top:809px;font-size:12px">HPF</div>
  <div class="abs led" style="left:243px;top:841px"></div>
  <div class="abs field" style="left:262px;top:827px;width:83px">Off</div>
  <div class="abs select" style="left:350px;top:827px;width:170px">Butterworth 6dB</div>

  <!-- EQ bands: right block -->
  <div class="abs col-head" style="left:549px;top:609px">On</div>
  <div class="abs col-head" style="left:588px;top:609px;transform:none">Type</div>
  <div class="abs col-head" style="left:679px;top:609px">Freq</div>
  <div class="abs col-head" style="left:754px;top:609px">Q</div>
  <div class="abs col-head" style="left:804px;top:609px">Gain</div>

  <div class="abs led on" style="left:549px;top:645px"></div>
  <div class="abs select" style="left:568px;top:631px;width:87px">Bell</div>
  <div class="abs field" style="left:661px;top:631px;width:65px">20Hz</div>
  <div class="abs field" style="left:732px;top:631px;width:44px">1</div>
  <div class="abs field" style="left:782px;top:631px;width:45px">0dB</div>

  <div class="abs led" style="left:549px;top:678px"></div>
  <div class="abs select" style="left:568px;top:664px;width:87px">Notch</div>
  <div class="abs field" style="left:661px;top:664px;width:65px">20Hz</div>
  <div class="abs field" style="left:732px;top:664px;width:44px">1</div>
  <div class="abs field" style="left:782px;top:664px;width:45px">0dB</div>

  <div class="abs led" style="left:549px;top:712px"></div>
  <div class="abs select" style="left:568px;top:698px;width:87px">AllPass</div>
  <div class="abs field" style="left:661px;top:698px;width:65px">20Hz</div>
  <div class="abs field" style="left:732px;top:698px;width:44px">1</div>
  <div class="abs field" style="left:782px;top:698px;width:45px">0dB</div>

  <div class="abs led" style="left:549px;top:746px"></div>
  <div class="abs select" style="left:568px;top:732px;width:87px">Low Shelf</div>
  <div class="abs field" style="left:661px;top:732px;width:65px">20Hz</div>
  <div class="abs field" style="left:732px;top:732px;width:44px">1</div>
  <div class="abs field" style="left:782px;top:732px;width:45px">0dB</div>

  <div class="abs led" style="left:549px;top:779px"></div>
  <div class="abs select" style="left:568px;top:765px;width:87px">Band Pass</div>
  <div class="abs field" style="left:661px;top:765px;width:65px">20Hz</div>
  <div class="abs field" style="left:732px;top:765px;width:44px">1</div>
  <div class="abs field" style="left:782px;top:765px;width:45px">0dB</div>

  <div class="abs title" style="left:551px;top:809px;font-size:12px">LPF</div>
  <div class="abs led" style="left:549px;top:841px"></div>
  <div class="abs field" style="left:568px;top:827px;width:83px">Off</div>
  <div class="abs select" style="left:656px;top:827px;width:170px">Butterworth 6dB</div>
</div>
</body>
</html>
```